Bramble Café retail envelop design

This is a single serve coffee product for the adventurer consumer. The product is Fair Trade, Organic coffee grounds in a single serve pouch that can be used as a quality pour over drip brew while on the go. We would like to use designs that show adventure/hiking/camping with earth tones that display a organic/biodegradable feel.The open width of envelope film is 200mmThe finished bag size is W 100mm * L 120mm. (Once sealed)The eye mark size is W 10* H 5 mm. (side seam)Top/Bottom heat seal: 8mmSide heat seal: 7mmPlease use the samples provided as a guide only. I would like to see what you can come up with. Please use our original logo attached.Three blend varieties: Kelvermoor, Hollow, WarsawIG: @Bramblecafe

Target Market(s)

Adventurers, backpackers, campers, hikers, adventure riders, etc.

Colors

Designer to choose colors to be used in the design.

Requirements
Must have
• My Bramble Cafe logo, earthy feel (maybe black logo on earthy paper color backdrop?). Must show 12g size, instruction panel (this can be edited for visual appeal), IG account: Bramblecafe.
• Design will be printed in Matte finish.
Should not have
• It does not need all of the text that is shown on the back. I will prefer a more simplistic design rather than a crowded one.

```html
<!DOCTYPE html>
<html lang="en">
<head>
<meta charset="utf-8">
<title>Bramble Café – Kelvermoor single serve envelope</title>
<link rel="stylesheet" href="https://fonts.googleapis.com/css2?family=Lato:wght@400;700;900&family=Oswald:wght@500;600;700&display=swap">
<style>
  :root {
    --stage: #ececec;
    --sky-top: #c4d6d2;
    --sky-low: #e9e5d5;
    --ridge: #7fa59a;
    --forest: #2f6a5f;
    --forest-deep: #1c3b34;
    --frame: #1c3b34;
    --ink: #1f4640;
    --logo-ink: #111111;
    --card-line: #6f6f6f;
    --step-bar: #6b5a4c;
    --white: #ffffff;
  }
  * { box-sizing: border-box; margin: 0; padding: 0; }
  html, body { width: 1200px; height: 773px; overflow: hidden; }
  body { background: var(--stage); position: relative; font-family: "Lato", sans-serif; }

  .pouch {
    position: absolute; top: 91px; width: 492px; height: 591px; overflow: hidden;
    background: linear-gradient(180deg, var(--sky-top) 0%, var(--sky-low) 50%);
  }
  .pouch--front { left: 98px; }
  .pouch--back { left: 610px; }

  .landscape {
    position: absolute; left: 0; right: 0; top: 290px; bottom: 0;
    background: linear-gradient(180deg, rgba(127,165,154,0) 0%, var(--ridge) 18%, var(--forest) 52%, var(--forest-deep) 84%, var(--forest-deep) 100%);
  }

  .bracket { position: absolute; top: 123px; height: 398px; width: 80px; border: 10px solid var(--frame); }
  .bracket--left { border-right: none; }
  .bracket--right { border-left: none; }
  .pouch--front .bracket--left { left: 36px; }
  .pouch--front .bracket--right { right: 34px; }
  .pouch--back .bracket--left { left: 34px; width: 24px; }
  .pouch--back .bracket--right { right: 35px; width: 19px; }

  .brand-badge {
    position: absolute; left: 116px; top: 44px; width: 260px; height: 260px;
    border-radius: 50%; border: 7px solid var(--logo-ink);
    background: var(--sky-top);
    display: flex; align-items: center; justify-content: center;
  }
  .brand-badge__name {
    font-family: "Oswald", sans-serif; font-weight: 600; font-size: 40px;
    color: var(--logo-ink); text-transform: uppercase; text-align: center; line-height: 1.3;
  }

  .blend-name {
    position: absolute; left: 0; right: 0; top: 462px; text-align: center;
    font-family: "Oswald", sans-serif; font-weight: 700; font-size: 68px; letter-spacing: 1px; line-height: 1.2;
    color: var(--forest-deep); text-transform: uppercase;
    -webkit-text-stroke: 2px var(--white);
  }
  .net-weight {
    position: absolute; left: 0; right: 0; top: 556px; text-align: center;
    font-family: "Oswald", sans-serif; font-weight: 500; font-size: 14px; letter-spacing: 1px;
    color: var(--white);
  }

  .copy { position: absolute; text-align: center; color: var(--ink); font-size: 11.6px; line-height: 14.6px; }
  .copy--en { left: 54px; right: 54px; top: 42px; }
  .copy--fr { left: 72px; right: 72px; top: 166px; }
  .note-title { position: absolute; left: 0; right: 0; text-align: center; font-weight: 900; color: var(--ink); font-size: 25px; line-height: 1; }
  .note-title--en { top: 95px; }
  .note-title--fr { top: 131px; }
  .note-rule { position: absolute; left: 66px; width: 360px; top: 126px; height: 2px; background: var(--ink); }

  .steps {
    position: absolute; left: 56px; top: 261px; width: 380px; height: 108px;
    background: var(--white); display: flex; gap: 20px; padding: 10px 11px;
  }
  .step { width: 75px; height: 88px; border: 1px solid var(--card-line); border-radius: 3px; overflow: hidden; display: flex; flex-direction: column; }
  .step__art { flex: 1; background: linear-gradient(180deg, #f7f6f2, #e6e2d8); }
  .step__num { height: 14px; background: var(--step-bar); color: var(--white); font-size: 11px; font-style: italic; text-align: center; line-height: 14px; }

  .social { position: absolute; left: 56px; top: 478px; width: 70px; text-align: center; }
  .social__mark { width: 40px; height: 40px; margin: 0 auto 6px; border-radius: 50%; border: 3px solid var(--white); }
  .social__handle { color: var(--white); font-weight: 700; font-size: 10px; }

  .maker { position: absolute; left: 124px; width: 146px; top: 482px; text-align: right; font-family: "Oswald", sans-serif; font-weight: 600; font-size: 14px; line-height: 18px; color: var(--white); text-transform: uppercase; }
</style>
</head>
<body>
  <section class="pouch pouch--front" aria-label="Front of envelope">
    <div class="landscape" role="img" aria-label="Layered sage mountains and deep green pine forest landscape"></div>
    <div class="bracket bracket--left"></div>
    <div class="bracket bracket--right"></div>
    <div class="brand-badge"><span class="brand-badge__name">Bramble<br>Café</span></div>
    <h1 class="blend-name">Kelvermoor</h1>
    <p class="net-weight">12g</p>
  </section>

  <section class="pouch pouch--back" aria-label="Back of envelope">
    <div class="landscape" role="img" aria-label="Layered sage mountains and deep green pine forest landscape"></div>
    <div class="bracket bracket--left"></div>
    <div class="bracket bracket--right"></div>
    <p class="copy copy--en">Using Only Organic and Fair trade grounds weve made no sacrifice in taste, aroma, and quality all in a conveniently packaged single serve drip coffee that will allow you to say goodbye to instant coffees forever</p>
    <h2 class="note-title note-title--en">A Note to The Adventurous</h2>
    <div class="note-rule"></div>
    <h2 class="note-title note-title--fr">Une Notre aux Aventuriers</h2>
    <p class="copy copy--fr">En n'utilisant que des produits biologiques et issus du commerce equitable, nous n'avons fait aucun compromis sur le goilt, l'arame et la quantite dans un cafe goutte-a-goutte unique qui vous permettra de dire adieu aux cafes instantanes pour toujoursl</p>
    <div class="steps">
      <div class="step"><div class="step__art" role="img" aria-label="Tear open the drip pouch"></div><div class="step__num">1</div></div>
      <div class="step"><div class="step__art" role="img" aria-label="Hang the filter on the mug"></div><div class="step__num">2</div></div>
      <div class="step"><div class="step__art" role="img" aria-label="Pour hot water into the filter"></div><div class="step__num">3</div></div>
      <div class="step"><div class="step__art" role="img" aria-label="Remove the filter and enjoy"></div><div class="step__num">4</div></div>
    </div>
    <div class="social"><div class="social__mark"></div><p class="social__handle">@bramblecafe</p></div>
    <p class="maker">www.bramblecafe.com<br>Larkford, ON<br>Bramble Cafe.Inc</p>
  </section>
</body>
</html>
```